Tallow Microsystems PowerPoint Master Slide Deck Design

This is a 2-phase project to design a slide deck for a semiconductor company in the Silicon Valley. The design budget will be increased with each phase.
The slide deck will need to have one version with a dark background for presentations and a second version with a white background. Otherwise, the slides will be the same. I anticipate we will need a total of 10 slides, but that number may change.
The first phase will be to design a Title and a Title and Content slide.
- The Title Slide is the first slide of the deck. It should include the presentation title, the presenter's name and date of presentation
- The Title and Content slide should include a title and content with bullet points and up to 2 additional sub-bullets
- The Title and Content slide should have a footer that includes the slide #, Tallow Microsystems Confidential, and the logo. This footer will be on every slide except the Title Slide
The first two slides will serve as the format for the remaining ~8 slides:
-Header and Content Text (1, 2, 4 column)
-Header and Content Image (bar chart, pie chart, tables)
-Break
-Title only
-Closing (Tallow logo only)
Our slides contain a lot of content so a clean and simple design is best.
Both phases will need to include pre-set color options for
-Text and Lines
-Shadows
-Bullets and sub-bullets (including shapes, ex. circle, slash, square, etc.)
-Bar charts, pie charts, tables
Samples of our collateral are attached. Logo files are also attached
Look and feel
Each slider illustrates characteristics of the customer's brand and the style your logo design should communicate.

```html
<!DOCTYPE html>
<html lang="en">
<head>
<meta charset="utf-8">
<title>Tallow Microsystems — Master Slide Deck</title>
<link href="https://fonts.googleapis.com/css2?family=Inter:wght@400;500;600;700&display=swap" rel="stylesheet">
<style>
  :root{
    --page:#0d0d0d;
    --white:#ffffff;
    --ink:#111111;
    --muted:#555a66;
    --blue:#1a2ff0;
    --blue-deep:#1424c8;
    --cyan:#1fc4f2;
    --grey:#c9c9cc;
    --grey-dark:#a9a9ad;
    --navy:#0a0f74;
    --navy-deep:#050845;
    --break-grey:#d9d9db;
    --rule:#e3e3e6;
  }
  *{box-sizing:border-box;margin:0;padding:0}
  html,body{width:1200px;height:600px;overflow:hidden;background:var(--page)}
  body{font-family:"Inter",Arial,sans-serif}
  .board{position:relative;width:2576px;height:1288px;transform:scale(0.46584);transform-origin:0 0}
  .slide{position:absolute;width:498px;height:280px;overflow:hidden;background:var(--white);color:var(--ink)}
  .slide.dark{background:linear-gradient(160deg,#0a12a8 0%,var(--navy) 55%,var(--navy-deep) 100%);color:var(--white)}
  .slide.dark-flat{background:#0b1287;color:var(--white)}
  .accent{position:absolute;left:0;top:0;width:100%;height:3px;background:linear-gradient(90deg,var(--cyan),var(--blue))}

  /* wordmark stand-in */
  .mark{position:absolute;display:flex;align-items:center;gap:4px;font-weight:600;color:var(--blue)}
  .mark .dot{width:9px;height:9px;border-radius:50%;background:currentColor}
  .dark .mark,.dark-flat .mark{color:var(--white)}
  .mark-top{left:226px;top:36px;font-size:11px}
  .mark-big{font-size:19px;gap:7px}
  .mark-big .dot{width:15px;height:15px}

  /* title slides */
  .pres-title{position:absolute;left:226px;top:126px;font-size:19px;font-weight:700;color:var(--blue)}
  .dark .pres-title{color:var(--white)}
  .presenter{position:absolute;left:226px;top:158px;font-size:10px}
  .date{position:absolute;left:226px;top:233px;font-size:7px}
  .conf-small{position:absolute;left:226px;top:263px;font-size:3.6px;letter-spacing:.3px;opacity:.7;text-transform:uppercase}
  .decor{position:absolute}

  /* content slides */
  .slide-title{position:absolute;left:34px;top:24px;font-size:12.5px;font-weight:700}
  .content-heading{font-size:7px;color:var(--blue);margin-bottom:13px}
  .dark .content-heading{color:var(--cyan)}
  .body{font-size:5.6px;line-height:1.35;color:#222}
  .dark .body{color:#e6e8ff}
  .body p{margin-bottom:7px}
  .col{position:absolute;top:72px}
  .bullets{list-style:none;font-size:5.6px;line-height:1.35;color:#222}
  .dark .bullets{color:#e6e8ff}
  .bullets li{position:relative;padding-left:10px;margin-bottom:6px}
  .bullets li::before{content:"";position:absolute;left:0;top:2px;width:3px;height:3px;border-radius:50%;background:var(--blue)}
  .dark .bullets li::before{background:var(--cyan)}
  .bullets .l2{margin-left:12px}
  .bullets .l2::before{top:3px;width:6px;height:1px;border-radius:0}
  .bullets .l3{margin-left:24px}
  .bullets .l3::before{top:2px;width:3px;height:3px;border-radius:0;background:none;border:0.6px solid var(--blue)}
  .bullets .l4{margin-left:36px}
  .bullets .l4::before{top:2px;width:3px;height:3px;border-radius:0;background:none;border:0.6px solid #888}

  .footer{position:absolute;left:34px;right:34px;bottom:9px;display:flex;justify-content:space-between;align-items:center;font-size:3.6px;color:#8a8d96}
  .footer .conf{letter-spacing:.4px;text-transform:uppercase}
  .footer .fmark{font-size:5px;font-weight:600;color:var(--blue);display:flex;align-items:center;gap:2px}
  .footer .fmark i{width:4px;height:4px;border-radius:50%;background:currentColor}
  .dark .footer,.dark-flat .footer{color:#9aa1e6}
  .dark .footer .fmark,.dark-flat .footer .fmark{color:#6e8cff}

  /* tables */
  .grid-table{position:absolute;left:34px;top:66px;width:430px;border-collapse:collapse;font-size:5.6px}
  .grid-table th{color:var(--blue);font-weight:500;text-align:left;padding:4px 4px;border-bottom:1px solid var(--blue);font-size:6.5px}
  .grid-table td{height:22.5px;padding:0 4px;border:0.6px solid var(--rule);background:#f6f6f8;vertical-align:top;padding-top:3px}
  .grid-table td:first-child{background:#fff}
  .dark .grid-table th{color:var(--cyan);border:0.6px solid #4753c9;border-bottom:1px solid var(--cyan)}
  .dark .grid-table td{border-color:#4753c9;background:#1f2aa0}
  .dark .grid-table td:first-child{background:#131c8c}

  .legend{font-size:4.5px;display:flex;gap:5px;align-items:center}
  .legend span::before{content:"";display:inline-block;width:3px;height:3px;margin-right:2px;background:var(--c)}

  /* break */
  .break-title{position:absolute;left:283px;top:146px;font-size:15px;font-weight:700}
  .break-sub{position:absolute;left:283px;top:176px;font-size:9px}

  /* style guide */
  .sg-sub{position:absolute;left:34px;top:44px;font-size:5px;color:var(--cyan)}
  .sg-h{font-size:7px;font-weight:700;margin-bottom:6px}
  .sg-t{font-size:3.4px;line-height:1.35;color:#555}
  .swatches{display:grid;grid-template-columns:repeat(10,6.8px);gap:0.8px;background:#3a3a3e;padding:14px 3px 4px}
  .swatches i{height:6px;display:block}
  .highlight{background:var(--cyan);color:#fff;font-size:4px;padding:3px 4px;width:66px;margin-top:18px}
  .keymsg{border:1px solid var(--blue);color:var(--blue);font-size:4px;padding:3px 4px;width:66px;margin-top:4px;font-weight:600}
</style>
</head>
<body>
<div class="board">

  <!-- ROW 1 -->
  <section class="slide" style="left:28px;top:70px">
    <div class="decor" role="img" aria-label="Sweeping fibre-line graphic in blue and cyan" style="left:0;top:130px;width:210px;height:150px;background:radial-gradient(ellipse at 75% 10%,rgba(31,196,242,.35),rgba(26,47,240,.15) 45%,transparent 75%)"></div>
    <div class="decor" role="img" aria-label="Fibre-line graphic" style="left:130px;top:140px;width:60px;height:140px;background:linear-gradient(180deg,rgba(31,196,242,.25),rgba(26,47,240,.1))"></div>
    <div class="mark mark-top"><i class="dot"></i>Tallow</div>
    <h1 class="pres-title">Presentation title</h1>
    <p class="presenter">Presenter's name here</p>
    <p class="date">Date</p>
    <p class="conf-small">Tallow Microsystems Confidential</p>
  </section>

  <section class="slide" style="left:533px;top:70px">
    <div class="mark mark-top" style="left:32px"><i class="dot"></i>Tallow</div>
    <h1 class="pres-title" style="left:32px">Presentation title</h1>
    <p class="presenter" style="left:32px">Presenter's name here</p>
    <p class="date" style="left:32px">Date</p>
    <p class="conf-small" style="left:32px">Tallow Microsystems Confidential</p>
    <div class="decor" role="img" aria-label="Illustration of a hand holding a microchip" style="left:232px;top:80px;width:130px;height:200px;background:linear-gradient(180deg,#dcdce0 0%,#e9e9ec 60%,var(--cyan) 90%);border-radius:30px 30px 0 0"></div>
    <div class="decor" role="img" aria-label="Fibre-line graphic" style="left:400px;top:130px;width:98px;height:150px;background:radial-gradient(ellipse at 100% 60%,rgba(26,47,240,.35),rgba(31,196,242,.12) 55%,transparent 80%)"></div>
  </section>

  <section class="slide" style="left:1039px;top:70px">
    <div class="accent"></div>
    <h2 class="slide-title">Style guide</h2>
    <p class="sg-sub">Well-crafted style guide to maintain consistent branding throughout the presentation</p>
    <div style="position:absolute;left:34px;top:62px;width:80px">
      <div class="sg-h">Theme colours</div>
      <div class="swatches">
        <i style="background:#fff"></i><i style="background:#111"></i><i style="background:#ccc"></i><i style="background:#1a2ff0"></i><i style="background:#1fc4f2"></i><i style="background:#0a0f74"></i><i style="background:#888"></i><i style="background:#aaa"></i><i style="background:#666"></i><i style="background:#ddd"></i>
        <i style="background:#eee"></i><i style="background:#555"></i><i style="background:#bbb"></i><i style="background:#5a6cf5"></i><i style="background:#8fe0f8"></i><i style="background:#3a42a0"></i><i style="background:#999"></i><i style="background:#c4c4c4"></i><i style="background:#777"></i><i style="background:#e5e5e5"></i>
        <i style="background:#ddd"></i><i style="background:#444"></i><i style="background:#999"></i><i style="background:#2838c0"></i><i style="background:#17a0c8"></i><i style="background:#070a50"></i><i style="background:#666"></i><i style="background:#888"></i><i style="background:#555"></i><i style="background:#c8c8c8"></i>
      </div>
      <div class="sg-h" style="margin-top:12px">Paragraph style</div>
      <div class="sg-t" style="color:var(--blue);font-size:4.5px">Paragraph heading in this blue</div>
      <div class="sg-t" style="margin-top:8px">Paragraph heading is always 2 points bigger in font size than the body content. The body content should be in black colour with 1.0 line spacing</div>
    </div>
    <div style="position:absolute;left:128px;top:62px;width:80px">
      <div class="sg-h">Bold text colour</div>
      <div class="sg-t">Bold text colour within the content is <b>Black</b> or you can use even the <b style="color:var(--blue)">bright blue</b> to highlight the keyword</div>
      <div class="sg-h" style="margin-top:22px">Font</div>
      <div class="sg-t">Inter regular for heading and body content</div>
      <div class="sg-t" style="margin-top:24px">This paragraph line separator should be the same colour for all the headings irrespective of the length of the sentence</div>
      <div class="highlight">Highlight colour</div>
      <div class="keymsg">Key message box</div>
    </div>
    <div style="position:absolute;left:221px;top:62px;width:140px">
      <div class="sg-h">Chart styles</div>
      <svg width="140" height="50" viewBox="0 0 140 50" aria-label="Sample charts">
        <g fill="var(--blue)"><rect x="10" y="20" width="3" height="16"/><rect x="22" y="25" width="3" height="11"/><rect x="34" y="22" width="3" height="14"/><rect x="46" y="19" width="3" height="17"/></g>
        <g fill="var(--cyan)"><rect x="14" y="27" width="3" height="9"/><rect x="26" y="19" width="3" height="17"/><rect x="38" y="29" width="3" height="7"/><rect x="50" y="25" width="3" height="11"/></g>
        <g fill="var(--grey)"><rect x="18" y="29" width="3" height="7"/><rect x="30" y="29" width="3" height="7"/><rect x="42" y="25" width="3" height="11"/><rect x="54" y="17" width="3" height="19"/></g>
        <circle cx="100" cy="28" r="10" fill="none" stroke="var(--grey-dark)" stroke-width="10" />
        <circle cx="100" cy="28" r="10" fill="none" stroke="var(--blue)" stroke-width="10" stroke-dasharray="20 43" transform="rotate(20 100 28)"/>
        <circle cx="100" cy="28" r="10" fill="none" stroke="var(--cyan)" stroke-width="10" stroke-dasharray="10 53" transform="rotate(-60 100 28)"/>
      </svg>
      <div class="sg-h" style="margin-top:10px">Line style</div>
      <div class="sg-t">Divider line style is ACC3 with 0.5pt thickness</div>
      <div class="sg-h" style="margin-top:14px">Gradient style</div>
      <div style="display:flex;gap:6px">
        <div><div style="width:56px;height:7px;background:linear-gradient(90deg,var(--cyan),var(--blue))"></div><div style="width:56px;height:7px;margin-top:2px;background:linear-gradient(90deg,var(--blue),var(--navy-deep))"></div></div>
        <div class="sg-t">The angle of these gradients can be changed using the gradient options</div>
      </div>
      <div style="display:flex;gap:6px;margin-top:12px;align-items:center">
        <div style="width:28px;height:1px;background:#333"></div>
        <div class="sg-t"><b style="color:#222">Call out style</b><br>Callouts from a paragraph are created using this pointer</div>
      </div>
    </div>
    <div style="position:absolute;left:381px;top:62px;width:96px">
      <div class="sg-h">Image effects</div>
      <div role="img" aria-label="Sample slide thumbnails showing image treatments" style="width:30px;height:102px;background:linear-gradient(180deg,#eef0fb 0%,#eef0fb 28%,var(--blue) 30%,#1d2ab0 65%,var(--navy-deep) 100%)"></div>
      <div class="sg-t" style="position:absolute;left:36px;top:14px;width:58px">This image style is used within the slides for images and photographs. Keep the treatment consistent.</div>
      <div class="sg-t" style="margin-top:8px"><b style="color:#222">Illustrations</b><br>Flat vector graphic style</div>
      <div class="sg-t" style="margin-top:4px"><b style="color:#222">Iconography</b><br>Simple line icons in blue</div>
    </div>
    <footer class="footer"><span>3</span><span class="conf">Tallow Microsystems Confidential</span><span class="fmark"><i></i>Tallow</span></footer>
  </section>

  <section class="slide" style="left:1544px;top:70px">
    <div class="accent"></div>
    <h2 class="slide-title">Slide title</h2>
    <div class="col" style="left:34px;width:430px">
      <div class="content-heading">Heading of content</div>
      <ul class="bullets">
        <li>Lorem ipsum dolor sit amet, consectetuer adipiscing elit. Maecenas porttitor congue massa. Fusce posuere, magna sed pulvinar ultricies, purus lectus malesuada libero, sit amet commodo magna eros quis urna. Lorem ipsum dolor sit amet, consectetuer adipiscing elit. Maecenas porttitor congue massa. Fusce posuere, magna sed pulvinar ultricies, purus lectus malesuada libero, sit amet commodo magna eros quis urna.</li>
        <li class="l2">Nunc viverra imperdiet enim. Fusce est. Vivamus a tellus. Lorem ipsum dolor sit amet, consectetuer adipiscing elit. Maecenas porttitor congue massa. Fusce posuere, magna sed pulvinar ultricies, purus lectus malesuada libero, sit amet commodo magna eros quis urna.</li>
        <li class="l3">Pellentesque habitant morbi tristique senectus et netus et malesuada fames ac turpis egestas. Proin pharetra nonummy pede. Mauris et orci. Lorem ipsum dolor sit amet, consectetuer adipiscing elit. Maecenas porttitor congue massa. Fusce posuere, magna sed pulvinar ultricies, purus lectus malesuada libero, sit amet commodo magna eros quis urna.</li>
        <li class="l4">senectus et netus et malesuada fames ac turpis egestas. Proin pharetra nonummy pede. Mauris et Lorem ipsum dolor sit amet, consectetuer adipiscing elit. Maecenas porttitor congue massa. Fusce posuere, magna sed pulvinar ultricies, purus lectus malesuada libero, sit amet commodo magna eros quis urna.</li>
      </ul>
    </div>
    <footer class="footer"><span>4</span><span class="conf">Tallow Microsystems Confidential</span><span class="fmark"><i></i>Tallow</span></footer>
  </section>

  <section class="slide" style="left:2049px;top:70px">
    <div class="accent"></div>
    <h2 class="slide-title">Slide title</h2>
    <div class="col" style="left:34px;width:195px">
      <div class="content-heading">Heading of content</div>
      <div class="body"><p>Lorem ipsum dolor sit amet, consectetuer adipiscing elit. Maecenas porttitor congue massa. Fusce posuere, magna sed pulvinar ultricies, purus lectus malesuada libero, sit amet commodo magna eros quis urna.</p><p>Nunc viverra imperdiet enim. Fusce est. Vivamus a tellus.</p><p>Pellentesque habitant morbi tristique senectus et netus et malesuada fames ac turpis egestas. Proin pharetra nonummy pede. Mauris et orci.</p><p>Lorem ipsum dolor sit amet, consectetuer adipiscing elit. Maecenas porttitor congue massa. Fusce posuere, magna sed pulvinar ultricies, purus lectus malesuada libero, sit amet commodo magna eros quis urna.</p><p>Nunc viverra imperdiet enim. Fusce est. Vivamus a tellus.</p></div>
    </div>
    <div class="col" style="left:276px;width:195px">
      <div class="content-heading">Heading of content</div>
      <div class="body"><p>Lorem ipsum dolor sit amet, consectetuer adipiscing elit. Maecenas porttitor congue massa. Fusce posuere, magna sed pulvinar ultricies, purus lectus malesuada libero, sit amet commodo magna eros quis urna.</p><p>Nunc viverra imperdiet enim. Fusce est. Vivamus a tellus.</p><p>Pellentesque habitant morbi tristique senectus et netus et malesuada fames ac turpis egestas. Proin pharetra nonummy pede. Mauris et orci.</p><p>Lorem ipsum dolor sit amet, consectetuer adipiscing elit. Maecenas porttitor congue massa. Fusce posuere, magna sed pulvinar ultricies, purus lectus malesuada libero, sit amet commodo magna eros quis urna.</p><p>Nunc viverra imperdiet enim. Fusce est. Vivamus a tellus.</p></div>
    </div>
    <footer class="footer"><span>5</span><span class="conf">Tallow Microsystems Confidential</span><span class="fmark"><i></i>Tallow</span></footer>
  </section>

  <!-- ROW 2 -->
  <section class="slide" style="left:28px;top:360px">
    <div class="accent"></div>
    <h2 class="slide-title">Slide title</h2>
    <div class="col" style="left:34px;width:95px"><div class="content-heading">Heading of content</div><div class="body"><p>Lorem ipsum dolor sit amet, consectetuer adipiscing elit. Maecenas porttitor congue massa. Fusce posuere, magna sed pulvinar ultricies, purus lectus malesuada libero, sit amet commodo magna eros quis urna.</p><p>Nunc viverra imperdiet enim. Fusce est. Vivamus a tellus.</p><p>Pellentesque habitant morbi tristique senectus et netus et malesuada fames ac turpis egestas</p></div></div>
    <div class="col" style="left:147px;width:95px"><div class="content-heading">Heading of content</div><div class="body"><p>Lorem ipsum dolor sit amet, consectetuer adipiscing elit. Maecenas porttitor congue massa. Fusce posuere, magna sed pulvinar ultricies, purus lectus malesuada libero, sit amet commodo magna eros quis urna.</p><p>Nunc viverra imperdiet enim. Fusce est. Vivamus a tellus.</p><p>Pellentesque habitant morbi tristique senectus et netus et malesuada fames ac turpis egestas</p></div></div>
    <div class="col" style="left:260px;width:95px"><div class="content-heading">Heading of content</div><div class="body"><p>Lorem ipsum dolor sit amet, consectetuer adipiscing elit. Maecenas porttitor congue massa. Fusce posuere, magna sed pulvinar ultricies, purus lectus malesuada libero, sit amet commodo magna eros quis urna.</p><p>Nunc viverra imperdiet enim. Fusce est. Vivamus a tellus.</p><p>Pellentesque habitant morbi tristique senectus et netus et malesuada fames ac turpis egestas</p></div></div>
    <div class="col" style="left:373px;width:95px"><div class="content-heading">Heading of content</div><div class="body"><p>Lorem ipsum dolor sit amet, consectetuer adipiscing elit. Maecenas porttitor congue massa. Fusce posuere, magna sed pulvinar ultricies, purus lectus malesuada libero, sit amet commodo magna eros quis urna.</p><p>Nunc viverra imperdiet enim. Fusce est. Vivamus a tellus.</p><p>Pellentesque habitant morbi tristique senectus et netus et malesuada fames ac turpis egestas</p></div></div>
    <footer class="footer"><span>7</span><span class="conf">Tallow Microsystems Confidential</span><span class="fmark"><i></i>Tallow</span></footer>
  </section>

  <section class="slide" style="left:533px;top:360px">
    <div class="accent"></div>
    <h2 class="slide-title">Slide title</h2>
    <div class="col" style="left:34px;width:95px"><div class="content-heading">Heading of content</div><div class="body"><p>Lorem ipsum dolor sit amet, consectetuer adipiscing elit. Maecenas porttitor congue massa. Fusce posuere, magna sed pulvinar ultricies, purus lectus malesuada libero, sit amet commodo magna eros quis urna.</p><p>Nunc viverra imperdiet enim. Fusce est. Vivamus a tellus.</p><p>Pellentesque habitant morbi tristique senectus et netus et malesuada fames ac turpis egestas</p></div></div>
    <svg class="decor" style="left:160px;top:72px" width="300" height="170" viewBox="0 0 300 170" aria-label="Bar chart of three series across four categories">
      <g stroke="#e4e4e7" stroke-width="0.6"><line x1="14" y1="6" x2="295" y2="6"/><line x1="14" y1="29" x2="295" y2="29"/><line x1="14" y1="52" x2="295" y2="52"/><line x1="14" y1="75" x2="295" y2="75"/><line x1="14" y1="98" x2="295" y2="98"/><line x1="14" y1="121" x2="295" y2="121"/><line x1="14" y1="142" x2="295" y2="142" stroke="#bbb"/></g>
      <g font-size="5" fill="#777"><text x="4" y="8">6</text><text x="4" y="31">5</text><text x="4" y="54">4</text><text x="4" y="77">3</text><text x="4" y="100">2</text><text x="4" y="123">1</text><text x="4" y="144">0</text></g>
      <g fill="var(--blue)"><rect x="28" y="45" width="12" height="97"/><rect x="98" y="86" width="12" height="56"/><rect x="168" y="63" width="12" height="79"/><rect x="238" y="40" width="12" height="102"/></g>
      <g fill="var(--cyan)"><rect x="43" y="88" width="12" height="54"/><rect x="113" y="42" width="12" height="100"/><rect x="183" y="101" width="12" height="41"/><rect x="253" y="79" width="12" height="63"/></g>
      <g fill="#d9d9dc"><rect x="58" y="97" width="12" height="45"/><rect x="128" y="97" width="12" height="45"/><rect x="198" y="74" width="12" height="68"/><rect x="268" y="29" width="12" height="113"/></g>
      <g font-size="5.5" fill="#555" text-anchor="middle"><text x="49" y="152">Category 1</text><text x="119" y="152">Category 2</text><text x="189" y="152">Category 3</text><text x="259" y="152">Category 4</text></g>
    </svg>
    <div class="legend decor" style="left:262px;top:230px;color:#555"><span style="--c:var(--blue)">Series 1</span><span style="--c:var(--cyan)">Series 2</span><span style="--c:#d9d9dc">Series 3</span></div>
    <footer class="footer"><span>8</span><span class="conf">Tallow Microsystems Confidential</span><span class="fmark"><i></i>Tallow</span></footer>
  </section>

  <section class="slide" style="left:1039px;top:360px">
    <div class="accent"></div>
    <h2 class="slide-title">Slide title</h2>
    <div class="col" style="left:34px;width:95px"><div class="content-heading">Heading of content</div><div class="body"><p>Lorem ipsum dolor sit amet, consectetuer adipiscing elit. Maecenas porttitor congue massa. Fusce posuere, magna sed pulvinar ultricies, purus lectus malesuada libero, sit amet commodo magna eros quis urna.</p><p>Nunc viverra imperdiet enim. Fusce est. Vivamus a tellus.</p><p>Pellentesque habitant morbi tristique senectus et netus et malesuada fames ac turpis egestas</p></div></div>
    <div class="legend decor" style="left:228px;top:78px;color:#555"><span style="--c:var(--blue)">Category 1</span><span style="--c:var(--cyan)">Category 2</span><span style="--c:var(--grey-dark)">Category 3</span><span style="--c:#d9d9dc">Category 4</span></div>
    <svg class="decor" style="left:230px;top:88px" width="160" height="160" viewBox="0 0 160 160" aria-label="Donut chart of four categories">
      <g fill="none" stroke-width="20" transform="rotate(-90 80 80)">
        <circle cx="80" cy="80" r="47" stroke="var(--grey-dark)" stroke-dasharray="103 300"/>
        <circle cx="80" cy="80" r="47" stroke="var(--blue)" stroke-dasharray="0 103 90 300"/>
        <circle cx="80" cy="80" r="47" stroke="#d9d9dc" stroke-dasharray="0 193 58 300"/>
        <circle cx="80" cy="80" r="47" stroke="var(--cyan)" stroke-dasharray="0 251 45 300"/>
      </g>
    </svg>
    <footer class="footer"><span>9</span><span class="conf">Tallow Microsystems Confidential</span><span class="fmark"><i></i>Tallow</span></footer>
  </section>

  <section class="slide" style="left:1544px;top:360px">
    <div class="accent"></div>
    <h2 class="slide-title">Slide title</h2>
    <table class="grid-table">
      <tr><th>Text</th><th>Text</th><th>Text</th><th>Text</th><th>Text</th><th>Text</th><th>Text</th><th>Text</th><th>Text</th><th>Text</th></tr>
      <tr><td>Text</td><td></td><td></td><td></td><td></td><td></td><td></td><td></td><td></td><td></td></tr>
      <tr><td>Text</td><td></td><td></td><td></td><td></td><td></td><td></td><td></td><td></td><td></td></tr>
      <tr><td>Text</td><td></td><td></td><td></td><td></td><td></td><td></td><td></td><td></td><td></td></tr>
      <tr><td>Text</td><td></td><td></td><td></td><td></td><td></td><td></td><td></td><td></td><td></td></tr>
      <tr><td>Text</td><td></td><td></td><td></td><td></td><td></td><td></td><td></td><td></td><td></td></tr>
      <tr><td>Text</td><td></td><td></td><td></td><td></td><td></td><td></td><td></td><td></td><td></td></tr>
      <tr><td>Text</td><td></td><td></td><td></td><td></td><td></td><td></td><td></td><td></td><td></td></tr>
    </table>
    <footer class="footer"><span>10</span><span class="conf">Tallow Microsystems Confidential</span><span class="fmark"><i></i>Tallow</span></footer>
  </section>

  <section class="slide" style="left:2049px;top:360px;background:var(--break-grey)">
    <div class="decor" role="img" aria-label="Flowing fibre-line graphic in cyan and white" style="left:0;top:0;width:260px;height:280px;background:radial-gradient(ellipse at 55% 70%,rgba(31,196,242,.35),rgba(255,255,255,.35) 45%,transparent 75%)"></div>
    <h2 class="break-title">Break slide</h2>
    <p class="break-sub">Subtitle here</p>
    <footer class="footer"><span>11</span><span class="conf">Tallow Microsystems Confidential</span><span class="fmark"><i></i>Tallow</span></footer>
  </section>

  <!-- ROW 3 -->
  <section class="slide" style="left:28px;top:648px">
    <div class="mark mark-big" style="left:190px;top:126px"><i class="dot"></i>Tallow</div>
  </section>

  <section class="slide dark" style="left:533px;top:648px">
    <div class="decor" role="img" aria-label="Fibre-line graphic in cyan and white" style="left:0;top:130px;width:190px;height:150px;background:radial-gradient(ellipse at 85% 40%,rgba(130,200,255,.4),rgba(31,196,242,.12) 50%,transparent 78%)"></div>
    <div class="mark mark-top"><i class="dot"></i>Tallow</div>
    <h1 class="pres-title">Presentation title</h1>
    <p class="presenter">Presenter's name here</p>
    <p class="date">Date</p>
    <p class="conf-small">Tallow Microsystems Confidential</p>
  </section>

  <section class="slide dark" style="left:1039px;top:648px">
    <div class="mark mark-top" style="left:32px"><i class="dot"></i>Tallow</div>
    <h1 class="pres-title" style="left:32px">Presentation title</h1>
    <p class="presenter" style="left:32px">Presenter's name here</p>
    <p class="date" style="left:32px">Date</p>
    <p class="conf-small" style="left:32px">Tallow Microsystems Confidential</p>
    <div class="decor" role="img" aria-label="Illustration of a hand holding a microchip" style="left:232px;top:80px;width:130px;height:200px;background:linear-gradient(180deg,#d7d9e6 0%,#e9e9ef 60%,var(--cyan) 90%);border-radius:30px 30px 0 0"></div>
    <div class="decor" role="img" aria-label="Fibre-line graphic" style="left:400px;top:120px;width:98px;height:160px;background:radial-gradient(ellipse at 100% 60%,rgba(160,220,255,.35),rgba(31,196,242,.1) 55%,transparent 80%)"></div>
  </section>

  <section class="slide dark" style="left:1544px;top:648px">
    <div class="decor" role="img" aria-label="Photograph of a circuit board with a processor chip in blue light" style="inset:0;background:radial-gradient(ellipse at 55% 55%,#3a48d8 0%,#1d2ab8 40%,#0b1280 100%)"></div>
    <div class="decor" role="img" aria-label="Fibre-line graphic" style="left:380px;top:120px;width:118px;height:160px;background:radial-gradient(ellipse at 100% 60%,rgba(200,220,255,.35),transparent 75%)"></div>
    <div class="mark mark-top" style="left:32px"><i class="dot"></i>Tallow</div>
    <h1 class="pres-title" style="left:32px">Presentation title</h1>
    <p class="presenter" style="left:32px">Presenter's name here</p>
    <p class="date" style="left:32px">Date</p>
    <p class="conf-small" style="left:32px">Tallow Microsystems Confidential</p>
  </section>

  <section class="slide dark" style="left:2049px;top:648px;background:linear-gradient(180deg,#0b1287,#070b5e)">
    <div class="accent"></div>
    <h2 class="slide-title">Slide title</h2>
    <div class="col" style="left:34px;width:430px">
      <div class="content-heading">Heading of content</div>
      <ul class="bullets">
        <li>Lorem ipsum dolor sit amet, consectetuer adipiscing elit. Maecenas porttitor congue massa. Fusce posuere, magna sed pulvinar ultricies, purus lectus malesuada libero, sit amet commodo magna eros quis urna. Lorem ipsum dolor sit amet, consectetuer adipiscing elit. Maecenas porttitor congue massa. Fusce posuere, magna sed pulvinar ultricies, purus lectus malesuada libero, sit amet commodo magna eros quis urna.</li>
        <li class="l2">Nunc viverra imperdiet enim. Fusce est. Vivamus a tellus. Lorem ipsum dolor sit amet, consectetuer adipiscing elit. Maecenas porttitor congue massa. Fusce posuere, magna sed pulvinar ultricies, purus lectus malesuada libero, sit amet commodo magna eros quis urna.</li>
        <li class="l3">Pellentesque habitant morbi tristique senectus et netus et malesuada fames ac turpis egestas. Proin pharetra nonummy pede. Mauris et orci. Lorem ipsum dolor sit amet, consectetuer adipiscing elit. Maecenas porttitor congue massa. Fusce posuere, magna sed pulvinar ultricies, purus lectus malesuada libero, sit amet commodo magna eros quis urna.</li>
        <li class="l4">senectus et netus et malesuada fames ac turpis egestas. Proin pharetra nonummy pede. Mauris et Lorem ipsum dolor sit amet, consectetuer adipiscing elit. Maecenas porttitor congue massa. Fusce posuere, magna sed pulvinar ultricies, purus lectus malesuada libero, sit amet commodo magna eros quis urna.</li>
      </ul>
    </div>
    <footer class="footer"><span>15</span><span class="conf">Tallow Microsystems Confidential</span><span class="fmark"><i></i>Tallow</span></footer>
  </section>

  <!-- ROW 4 -->
  <section class="slide dark" style="left:28px;top:937px;background:linear-gradient(180deg,#0b1287,#070b5e)">
    <div class="accent"></div>
    <h2 class="slide-title">Slide title</h2>
    <table class="grid-table" style="top:62px">
      <tr><th>Text</th><th>Text</th><th>Text</th><th>Text</th><th>Text</th><th>Text</th><th>Text</th><th>Text</th><th>Text</th><th>Text</th></tr>
      <tr><td>Text</td><td></td><td></td><td></td><td></td><td></td><td></td><td></td><td></td><td></td></tr>
      <tr><td>Text</td><td></td><td></td><td></td><td></td><td></td><td></td><td></td><td></td><td></td></tr>
      <tr><td>Text</td><td></td><td></td><td></td><td></td><td></td><td></td><td></td><td></td><td></td></tr>
      <tr><td>Text</td><td></td><td></td><td></td><td></td><td></td><td></td><td></td><td></td><td></td></tr>
      <tr><td>Text</td><td></td><td></td><td></td><td></td><td></td><td></td><td></td><td></td><td></td></tr>
      <tr><td>Text</td><td></td><td></td><td></td><td></td><td></td><td></td><td></td><td></td><td></td></tr>
      <tr><td>Text</td><td></td><td></td><td></td><td></td><td></td><td></td><td></td><td></td><td></td></tr>
    </table>
    <footer class="footer"><span>20</span><span class="conf">Tallow Microsystems Confidential</span><span class="fmark"><i></i>Tallow</span></footer>
  </section>

  <section class="slide dark" style="left:533px;top:937px;background:linear-gradient(180deg,#0b1287,#070b5e)">
    <div class="accent"></div>
    <h2 class="slide-title">Slide title</h2>
    <div class="col" style="left:34px;width:95px"><div class="content-heading">Heading of content</div><div class="body"><p>Lorem ipsum dolor sit amet, consectetuer adipiscing elit. Maecenas porttitor congue massa. Fusce posuere, magna sed pulvinar ultricies, purus lectus malesuada libero, sit amet commodo magna eros quis urna.</p><p>Nunc viverra imperdiet enim. Fusce est. Vivamus a tellus.</p><p>Pellentesque habitant morbi tristique senectus et netus et malesuada fames ac turpis egestas</p></div></div>
    <svg class="decor" style="left:160px;top:72px" width="300" height="170" viewBox="0 0 300 170" aria-label="Bar chart of three series across four categories">
      <g stroke="#3a45b8" stroke-width="0.6"><line x1="14" y1="6" x2="295" y2="6"/><line x1="14" y1="29" x2="295" y2="29"/><line x1="14" y1="52" x2="295" y2="52"/><line x1="14" y1="75" x2="295" y2="75"/><line x1="14" y1="98" x2="295" y2="98"/><line x1="14" y1="121" x2="295" y2="121"/><line x1="14" y1="142" x2="295" y2="142" stroke="#8a92e0"/></g>
      <g font-size="5" fill="#c8ccf5"><text x="4" y="8">6</text><text x="4" y="31">5</text><text x="4" y="54">4</text><text x="4" y="77">3</text><text x="4" y="100">2</text><text x="4" y="123">1</text><text x="4" y="144">0</text></g>
      <g fill="#1f38ff"><rect x="28" y="45" width="12" height="97"/><rect x="98" y="86" width="12" height="56"/><rect x="168" y="63" width="12" height="79"/><rect x="238" y="40" width="12" height="102"/></g>
      <g fill="var(--cyan)"><rect x="43" y="88" width="12" height="54"/><rect x="113" y="42" width="12" height="100"/><rect x="183" y="101" width="12" height="41"/><rect x="253" y="79" width="12" height="63"/></g>
      <g fill="#e4e4e8"><rect x="58" y="97" width="12" height="45"/><rect x="128" y="97" width="12" height="45"/><rect x="198" y="74" width="12" height="68"/><rect x="268" y="29" width="12" height="113"/></g>
      <g font-size="5.5" fill="#e6e8ff" text-anchor="middle"><text x="49" y="152">Category 1</text><text x="119" y="152">Category 2</text><text x="189" y="152">Category 3</text><text x="259" y="152">Category 4</text></g>
    </svg>
    <div class="legend decor" style="left:262px;top:230px;color:#e6e8ff"><span style="--c:#1f38ff">Series 1</span><span style="--c:var(--cyan)">Series 2</span><span style="--c:#e4e4e8">Series 3</span></div>
    <footer class="footer"><span>21</span><span class="conf">Tallow Microsystems Confidential</span><span class="fmark"><i></i>Tallow</span></footer>
  </section>

  <section class="slide dark" style="left:1039px;top:937px;background:linear-gradient(180deg,#0b1287,#070b5e)">
    <div class="accent"></div>
    <h2 class="slide-title">Slide title</h2>
    <div class="col" style="left:34px;width:95px"><div class="content-heading" style="color:#fff">Heading of content</div><div class="body"><p>Lorem ipsum dolor sit amet, consectetuer adipiscing elit. Maecenas porttitor congue massa. Fusce posuere, magna sed pulvinar ultricies, purus lectus malesuada libero, sit amet commodo magna eros quis urna.</p><p>Nunc viverra imperdiet enim. Fusce est. Vivamus a tellus.</p><p>Pellentesque habitant morbi tristique senectus et netus et malesuada fames ac turpis egestas</p></div></div>
    <div class="legend decor" style="left:228px;top:78px;color:#e6e8ff"><span style="--c:#1f38ff">Category 1</span><span style="--c:var(--cyan)">Category 2</span><span style="--c:var(--grey-dark)">Category 3</span><span style="--c:#e4e4e8">Category 4</span></div>
    <svg class="decor" style="left:230px;top:88px" width="160" height="160" viewBox="0 0 160 160" aria-label="Donut chart of four categories">
      <g fill="none" stroke-width="20" transform="rotate(-90 80 80)">
        <circle cx="80" cy="80" r="47" stroke="var(--grey-dark)" stroke-dasharray="103 300"/>
        <circle cx="80" cy="80" r="47" stroke="#1f38ff" stroke-dasharray="0 103 90 300"/>
        <circle cx="80" cy="80" r="47" stroke="#e4e4e8" stroke-dasharray="0 193 58 300"/>
        <circle cx="80" cy="80" r="47" stroke="var(--cyan)" stroke-dasharray="0 251 45 300"/>
      </g>
    </svg>
    <footer class="footer"><span>22</span><span class="conf">Tallow Microsystems Confidential</span><span class="fmark"><i></i>Tallow</span></footer>
  </section>

  <section class="slide dark" style="left:1544px;top:937px;background:linear-gradient(170deg,#1a2ae0 0%,#0b1394 50%,#02031e 100%)">
    <div class="decor" role="img" aria-label="Flowing fibre-line graphic in deep blue" style="left:0;top:0;width:260px;height:280px;background:radial-gradient(ellipse at 45% 70%,rgba(60,110,255,.4),transparent 70%)"></div>
    <h2 class="break-title">Break slide</h2>
    <p class="break-sub">Subtitle here</p>
    <footer class="footer"><span>19</span><span class="conf">Tallow Microsystems Confidential</span><span class="fmark"><i></i>Tallow</span></footer>
  </section>

  <section class="slide dark-flat" style="left:2049px;top:937px">
    <div class="mark mark-big" style="left:190px;top:126px"><i class="dot"></i>Tallow</div>
  </section>

</div>
</body>
</html>
```